Business Card Design

I am starting my therapy private practice. I will be an in home therapist, so I go into family's homes instead of using an office to do family/marriage therapy. Therefore, I do not have an office address. I am looking for something in the black, red, gray, and blue color scheme that appeals to both families, couples and teenagers.

Industry/Entity Type

Business

Contact Information for Business Card

Lena Brightwell, MS, MFT Intern
Marriage and Family Therapy
In Home Therapist
617-482-5190
Lena@LenaBrightwell-example.com

```html
<!DOCTYPE html>
<html lang="en">
<head>
<meta charset="utf-8">
<title>Lena Brightwell – Business Card</title>
<link rel="stylesheet" href="https://fonts.googleapis.com/css2?family=Cinzel:wght@500;700&family=Alegreya+Sans:wght@400;500&display=swap">
<style>
  :root {
    --page-bg: #e4e2df;
    --red-deep: #8e0a10;
    --red-mid: #c8141c;
    --red-bright: #e8262e;
    --stripe: rgba(255, 140, 140, 0.45);
    --band-black: #111111;
    --base-mauve: #8f4f55;
    --base-mauve-light: #a0636a;
    --name-red: #c3141c;
    --text-light: #efe6e6;
    --icon-red: #c8141c;
  }
  * { margin: 0; padding: 0; box-sizing: border-box; }
  html, body {
    width: 1200px;
    height: 1000px;
    overflow: hidden;
    background: var(--page-bg);
  }
  .canvas {
    width: 1200px;
    height: 1000px;
    display: flex;
    align-items: center;
    justify-content: center;
  }
  .business-card {
    position: relative;
    width: 1050px;
    height: 600px;
    overflow: hidden;
    background: var(--base-mauve);
    box-shadow: 0 10px 30px rgba(0,0,0,0.25);
  }
  .card-top {
    position: absolute;
    left: 0; top: 0;
    width: 100%;
    height: 332px;
    background:
      repeating-linear-gradient(to bottom, transparent 0 26px, var(--stripe) 26px 29px),
      radial-gradient(ellipse at 62% 70%, var(--red-bright) 0%, var(--red-mid) 40%, var(--red-deep) 100%);
  }
  .divider-band {
    position: absolute;
    left: 0; top: 332px;
    width: 100%;
    height: 14px;
    background: var(--band-black);
  }
  .card-bottom {
    position: absolute;
    left: 0; top: 346px;
    width: 100%;
    height: 254px;
    background: radial-gradient(ellipse at 40% 40%, var(--base-mauve-light) 0%, var(--base-mauve) 70%);
  }
  .tree-emblem {
    position: absolute;
    left: 510px;
    top: 70px;
    width: 200px;
    height: 262px;
  }
  .contact {
    position: absolute;
    left: 60px;
    top: 370px;
    right: 40px;
    color: var(--text-light);
    font-family: "Alegreya Sans", sans-serif;
  }
  .name-line {
    font-family: "Cinzel", serif;
    font-weight: 500;
    font-size: 40px;
    color: var(--name-red);
    letter-spacing: 1px;
    text-shadow: 0 1px 0 rgba(255,255,255,0.25), 0 -1px 1px rgba(0,0,0,0.35);
    white-space: nowrap;
  }
  .services {
    margin-top: 6px;
    font-size: 32px;
    white-space: nowrap;
  }
  .services .dot { color: var(--icon-red); margin: 0 6px; }
  .details {
    position: relative;
    height: 110px;
    margin-top: 4px;
  }
  .detail {
    position: absolute;
    display: flex;
    align-items: center;
    gap: 12px;
    font-size: 32px;
    white-space: nowrap;
  }
  .detail svg { width: 22px; height: 22px; flex: none; }
  .detail-phone { left: 0; top: 0; }
  .detail-email { left: 380px; top: 54px; }
</style>
</head>
<body>
<main class="canvas">
  <section class="business-card">
    <div class="card-top"></div>
    <svg class="tree-emblem" viewBox="0 0 200 262" role="img" aria-label="Stylised tree with a black trunk and round red foliage">
      <defs>
        <radialGradient id="tree-tone" cx="50%" cy="35%" r="60%">
          <stop offset="0%" stop-color="#d0161e"/>
          <stop offset="100%" stop-color="#5a0a0c" stop-opacity="0.85"/>
        </radialGradient>
      </defs>
      <rect x="0" y="0" width="200" height="262" rx="90" fill="url(#tree-tone)"/>
    </svg>
    <div class="divider-band"></div>
    <div class="card-bottom"></div>

    <div class="contact">
      <h1 class="name-line">Lena Brightwell, MS, MFT Intern</h1>
      <p class="services">Marriage and Family Therapy<span class="dot">•</span>In Home Therapist</p>
      <div class="details">
        <p class="detail detail-phone">
          <svg viewBox="0 0 22 22" aria-hidden="true">
            <rect width="22" height="22" rx="3" fill="var(--icon-red)"/>
            <path d="M6 8 C6 6 8 5 11 5 C14 5 16 6 16 8 L14 9 L13 7.5 C12 7.2 10 7.2 9 7.5 L8 9 Z M7 11 L15 11 L16 17 L6 17 Z" fill="#5a0a0c"/>
          </svg>
          617-482-5190
        </p>
        <p class="detail detail-email">
          <svg viewBox="0 0 22 22" aria-hidden="true">
            <rect width="22" height="22" rx="3" fill="var(--icon-red)"/>
            <rect x="4" y="6" width="14" height="10" fill="none" stroke="#5a0a0c" stroke-width="1.6"/>
            <path d="M4 6 L11 12 L18 6" fill="none" stroke="#5a0a0c" stroke-width="1.6"/>
          </svg>
          Lena@LenaBrightwell-example.com
        </p>
      </div>
    </div>
  </section>
</main>
</body>
</html>
```